CD Label Design Project

I need a CD label (circular) designed for a new company called DuctProfitPath.com. The CD is for an interview that has been done that will be mailed out to prospects who join the mailing list.
The CD itself is titled “The 9 hidden sales traps that Furnace Shop Founders Miss.”

This title will need to be on the cd. The business itself is a marketing and coaching business for HVAC business owners so a design that communicates professionalism and business growth is essential. Ideally using colours from the logo in the design.
Updates

Just a quick note, the brief wasn't entirely clear. The design is for a CD label (circular) not a square cover. Thanks everyone.

Target Market(s)

HVAC (heating and cooling) business owners

Industry/Entity Type

Marketing

Requirements
Must have
• The title of the cd
Should not have
• images of heating or cooling systems
no images of money of cash

```html
<!DOCTYPE html>
<html lang="en">
<head>
<meta charset="utf-8">
<title>DuctProfitPath.com – CD Label</title>
<link rel="stylesheet" href="https://fonts.googleapis.com/css2?family=Kalam:wght@400;700&display=swap">
<style>
  :root {
    --page-bg: #f2f2f2;
    --frame-edge: #ff3f00;
    --frame-mid: #ff7a00;
    --panel-light: #7f7f80;
    --panel-mid: #4a5a72;
    --panel-dark: #15305a;
    --title-ink: #1c64b0;
    --title-outline: #0d3a6e;
    --title-glow: rgba(120, 175, 235, 0.55);
    --brand-ink: #d9dee6;
    --hub-ring: #9aa6b6;
    --hole: #f2f2f2;
  }
  html, body {
    margin: 0;
    padding: 0;
    width: 1200px;
    height: 1200px;
    overflow: hidden;
    background: var(--page-bg);
  }
  .label {
    position: absolute;
    left: 20px;
    top: 20px;
    width: 1160px;
    height: 1160px;
    border-radius: 50%;
    background: radial-gradient(circle at 50% 50%, var(--frame-mid) 0%, var(--frame-mid) 88%, var(--frame-edge) 100%);
    font-family: "Kalam", "Comic Sans MS", cursive;
  }
  .face {
    position: absolute;
    left: 40px;
    top: 40px;
    width: 1080px;
    height: 1080px;
    border-radius: 50%;
    overflow: hidden;
    background: linear-gradient(135deg, var(--panel-light) 0%, var(--panel-mid) 45%, var(--panel-dark) 100%);
  }
  .title {
    position: absolute;
    left: 0;
    top: 166px;
    width: 100%;
    margin: 0;
    text-align: center;
    font-weight: 700;
    font-size: 64px;
    line-height: 86px;
    color: var(--title-ink);
    text-shadow:
      -1px -1px 0 var(--title-outline), 1px -1px 0 var(--title-outline),
      -1px 1px 0 var(--title-outline), 1px 1px 0 var(--title-outline),
      0 0 8px var(--title-glow);
  }
  .title-line { display: block; white-space: nowrap; }
  .hub {
    position: absolute;
    left: 400px;
    top: 400px;
    width: 280px;
    height: 280px;
    border-radius: 50%;
    border: 3px solid var(--hub-ring);
    box-sizing: border-box;
  }
  .hole {
    position: absolute;
    left: 465px;
    top: 465px;
    width: 150px;
    height: 150px;
    border-radius: 50%;
    background: var(--hole);
  }
  .brand {
    position: absolute;
    left: 0;
    top: 760px;
    width: 100%;
    display: flex;
    justify-content: center;
    align-items: center;
    gap: 14px;
    font-weight: 700;
    font-size: 48px;
    color: var(--brand-ink);
  }
  .brand-mark {
    width: 22px;
    height: 22px;
    border-radius: 50%;
    background: var(--frame-mid);
  }
</style>
</head>
<body>
  <main class="label">
    <section class="face">
      <h1 class="title">
        <span class="title-line">The 9 hidden sales traps</span>
        <span class="title-line">that Furnace Shop</span>
        <span class="title-line">Founders Miss.</span>
      </h1>
      <div class="hub" aria-hidden="true"></div>
      <div class="hole" aria-hidden="true"></div>
      <div class="brand">
        <span class="brand-mark" aria-hidden="true"></span>
        <span class="brand-name">DuctProfitPath.com</span>
      </div>
    </section>
  </main>
</body>
</html>
```